Lotus Ridge Website

We need a website that has clean, asian looking images that relax and motivate people to come into our integrated medical center. My current website is www.needlebalmclinic.com and I would like the design for Lotus Ridge Health Solutions to be similar but more inviting with video content and a product purchase store as well. A moving banner would be nice too. When people are looking for ways of losing weight or getting out of pain we want them to make the connection that we have the solution. This website needs to provide sufficient information so that patients are well informed and choose us as their health provider before they ever walk through our doors. We offer comprehensive natural medicine that is based on the principles that the body can heal itself when given the right conditions. Our services include medical weight loss and hormone balancing, acupuncture and chinese herbal medicine, physical medicine, trigger point injections, allergy testing and joint rehabilitation. The Medical Doctor and Licensed Acupuncturist work as a team to provide optimal care that is catered to each individual who comes through our doors.
Updates

Target Market(s)

40 to 50 year olds who want to lose weight or have pain issues.

Industry/Entity Type

Medical

Requirements
Must have
• Use photos from our website www.needlebalmclinic.com or similar content. Video content. Moving banner with relaxing images.
Nice to have
• Happy, healthy looking people. Medical Doctors working as a team. Friendly staff in a cutting edge facility.
Should not have
• Papyrus font, or big bold words.

```html
<!DOCTYPE html>
<html lang="en">
<head>
<meta charset="utf-8">
<title>Lotus Ridge Acupuncture</title>
<link href="https://fonts.googleapis.com/css2?family=Ubuntu:wght@300;400;500&family=Ubuntu+Condensed&display=swap" rel="stylesheet">
<style>
:root{
  --olive:#6b6a2a;
  --olive-dark:#55541e;
  --brown:#6e4631;
  --brown-dark:#5a3826;
  --rust:#a4502a;
  --text:#3b3b3b;
  --muted:#6d6d6d;
  --line:#e2e2e2;
  --wood:#4a2a1c;
  --green-btn:#7aa647;
}
*{box-sizing:border-box;margin:0;padding:0}
html,body{width:1061px;height:1200px;overflow:hidden;background:#fff;font-family:"Ubuntu",sans-serif;color:var(--text)}
.page{position:relative;width:1061px;height:1200px}
.abs{position:absolute}
.topline{left:0;top:0;width:100%;height:4px;background:var(--olive)}
.header{left:0;top:4px;width:100%;height:78px;background:linear-gradient(#fff 0%,#fff 45%,#f1f1e6 60%,#fbfbf4 100%);border-bottom:4px solid #eeeedd}
.logo{left:141px;top:0;width:115px;height:141px;background:var(--olive);border-radius:0 0 8px 8px;z-index:5;display:flex;flex-direction:column;align-items:center;justify-content:center;gap:6px}
.logo-mark{width:14px;height:14px;border-radius:50%;background:#fff}
.logo-name{color:#fff;font-weight:400;font-size:13px;text-align:center;line-height:1.25}
.phone{right:111px;top:14px;font-size:14px;color:#444}
.nav{left:262px;top:52px;display:flex;font-family:"Ubuntu Condensed",sans-serif;font-size:13.5px}
.nav a{color:#222;text-decoration:none;padding:0 13px;height:30px;line-height:24px;border-right:1px dotted #d8d8c8}
.nav a:last-child{border-right:0}
.nav a.active{color:var(--olive)}
.wood-l,.wood-r{top:90px;width:97px;height:317px;background:linear-gradient(90deg,#3c2015,#5b3423 40%,#452718 70%,#56311f)}
.wood-l{left:0}.wood-r{left:964px}
.arrow{top:218px;width:30px;height:50px}
.hero{left:97px;top:90px;width:867px;height:317px;background:linear-gradient(90deg,#fafafa 0%,#f1eeea 35%,#e8c9b0 60%,#e4bb9c 80%,#efe4da 100%)}
.quote{left:112px;top:166px;width:292px;font-size:14.5px;font-weight:300;line-height:21px;color:#333}
.quote-by{left:294px;top:268px;font-size:13px;color:var(--brown)}
.dots{left:106px;top:382px;display:flex;gap:12px;align-items:center}
.dots span{width:8px;height:8px;border-radius:50%;background:#444}
.dots .on{width:16px;height:16px;border:1.5px solid var(--rust);background:radial-gradient(var(--rust) 0 4px,#fff 5px)}
.welcome{left:110px;top:417px;font-size:21px;font-weight:300;color:#222}
.welcome em{font-style:normal;color:var(--rust);font-size:24px}
.subhead{left:112px;top:450px;font-size:14px;color:var(--olive-dark)}
.intro{left:112px;top:493px;width:525px;font-size:10.2px;line-height:21.2px;color:#444}
.fv-title{left:681px;top:421px;font-size:17px;font-weight:300;color:var(--rust)}
.fv-box{left:674px;top:451px;width:276px;height:192px;border:1px solid var(--line);padding:5px}
.fv-screen{width:100%;height:147px;background:linear-gradient(135deg,#7a4a2c,#d9a987 45%,#f2d6c0 65%,#6e4a30);position:relative}
.fv-bar{position:absolute;left:0;bottom:0;width:100%;height:26px;background:rgba(30,30,30,.85);display:flex;align-items:center;gap:6px;padding:0 6px;font-size:7px;color:#ddd}
.fv-play{width:26px;height:20px;background:#111;border:1px solid #555;display:flex;align-items:center;justify-content:center}
.fv-track{flex:1;height:6px;border:1px solid #888;background:#333}
.fv-foot{display:flex;justify-content:space-between;align-items:center;margin-top:6px}
.fv-lib{font-size:13px;font-weight:300;color:#777;line-height:12px}
.fv-lib small{display:block;font-size:9px;color:var(--green-btn)}
.fv-btn{background:linear-gradient(#8cb95a,#6a9a3c);color:#fff;font-size:7.5px;padding:6px 8px;border-radius:2px;display:flex;align-items:center;gap:6px}
.card{top:660px;width:257px}
.card-head{height:33px;background:var(--brown);border-radius:6px 6px 0 0;color:#fff;font-family:"Ubuntu Condensed",sans-serif;font-size:17px;line-height:36px;padding-left:13px}
.card-img{height:101px;border:1px solid #ddd;border-top:0;border-radius:0 0 6px 6px}
.card p{font-size:10px;line-height:16px;color:#555;padding:12px 3px 0}
.products-title{left:120px;top:868px;font-size:17px;color:var(--rust)}
.product{top:900px;width:185px;height:209px;border:1px solid var(--line);padding:8px}
.product-img{height:114px}
.product-name{margin-top:15px;font-size:10.5px;color:#555;font-weight:500;border-top:1px solid var(--line);padding-top:8px;margin-left:-8px;margin-right:-8px;padding-left:10px}
.product-sub{font-size:10px;color:#999;padding-left:2px}
.product-row{display:flex;justify-content:space-between;align-items:center;margin-top:10px}
.price{font-size:16px;font-style:italic;font-weight:300;color:var(--rust)}
.cart{background:var(--brown);color:#fff;font-size:10px;padding:6px 11px;border-radius:3px}
.footer{left:0;top:1149px;width:100%;height:51px;background:var(--brown)}
.foot-nav{left:143px;top:1158px;font-size:11.5px;color:#fff;word-spacing:2px}
.copy{left:143px;top:1180px;font-size:9px;color:#f0e4dc}
</style>
</head>
<body>
<div class="page">
  <div class="abs topline"></div>
  <div class="abs header"></div>
  <div class="abs logo"><span class="logo-mark"></span><span class="logo-name">Lotus Ridge<br>Acupuncture</span></div>
  <div class="abs phone">(555) 210-4830 &nbsp;OR&nbsp; (555) 318-2276</div>
  <nav class="abs nav">
    <a class="active">SO TAI HO</a><a>SEITAI SHINPO</a><a>ACUPUNCTURE</a><a>BIOGRAPHY</a><a>NUTRITION</a><a>MY JOURNEY</a><a>CONTANT US</a>
  </nav>

  <div class="abs wood-l" role="img" aria-label="Dark wood texture"></div>
  <div class="abs wood-r" role="img" aria-label="Dark wood texture"></div>
  <svg class="abs arrow" style="left:48px" viewBox="0 0 30 50"><polyline points="26,4 6,25 26,46" fill="none" stroke="#fff" stroke-width="5"/></svg>
  <svg class="abs arrow" style="left:980px" viewBox="0 0 30 50"><polyline points="4,4 24,25 4,46" fill="none" stroke="#fff" stroke-width="5"/></svg>
  <div class="abs hero" role="img" aria-label="Banner photo of a smiling woman relaxing during an acupuncture treatment"></div>
  <p class="abs quote">"The Doctor of the future will give no medi-cine but will interest patients in the care of the human frame, in diet, and in the cause and prevention of disease."</p>
  <p class="abs quote-by">Harold Whitcombe</p>
  <div class="abs dots"><span class="on"></span><span></span><span></span><span></span></div>

  <h1 class="abs welcome">Welcome to <em>Lotus Ridge Acupuncture</em></h1>
  <h2 class="abs subhead" style="font-weight:400">How does acupuncture work?</h2>
  <p class="abs intro">As the needles are carefully inserted into acupuncture points, specific cells stimulate nerve pathways that trigger a healing response to a particular organ system or area of the body. Acupuncture also acts on the auto-nomic nervous system and causes the release of endorphins, enkephalins and other natural pain relieving chemicals. At Lotus Ridge Acupuncture the system of acupuncture used is called Seitai Shinpo (which translates into "correct posture acupuncture method") that uses acupuncture and moxibustion to balance structural distortions by releasing tense areas of contraction along the spine. When the structure is properly balanced</p>

  <h3 class="abs fv-title" style="font-weight:300">Featured Video</h3>
  <div class="abs fv-box">
    <div class="fv-screen" role="img" aria-label="Video still of a woman receiving a herbal compress massage">
      <div class="fv-bar">
        <div class="fv-play"><svg width="10" height="12" viewBox="0 0 10 12"><polygon points="0,0 10,6 0,12" fill="#fff"/></svg></div>
        <span>00:00</span><div class="fv-track"></div>
        <svg width="10" height="10" viewBox="0 0 10 10"><path d="M1 1h3M1 1v3M9 1H6M9 1v3M1 9h3M1 9V6M9 9H6M9 9V6" stroke="#fff" stroke-width="1.4" fill="none"/></svg>
      </div>
    </div>
    <div class="fv-foot">
      <div class="fv-lib">VIDEO LIBRARY<small>GET TO KNOW US</small></div>
      <div class="fv-btn">CLICK HERE FOR MORE VIDEOS
        <svg width="14" height="11" viewBox="0 0 14 11"><rect x="1" y="1" width="12" height="7" fill="none" stroke="#fff" stroke-width="1.2"/><path d="M7 8v2M4 10.5h6" stroke="#fff"/></svg>
      </div>
    </div>
  </div>

  <div class="abs card" style="left:118px">
    <div class="card-head">SO THI HO</div>
    <div class="card-img" role="img" aria-label="Photo of a therapist massaging a woman's shoulders" style="background:linear-gradient(90deg,#f4ede6,#d9b08f 45%,#f0dccd)"></div>
    <p>Sotai ho is a system of movement therapy that was discovered after nearly 10 years of personal research from Hiroshi Tanabe, M.D. (1897-1993)</p>
  </div>
  <div class="abs card" style="left:401px">
    <div class="card-head">SEITAI SHINPO</div>
    <div class="card-img" role="img" aria-label="Photo of acupuncture needles placed on a woman's face" style="background:linear-gradient(90deg,#eef3f6,#e1c4ac 50%,#f3ece5)"></div>
    <p>Seitai Shinpo is a system of acupuncture developed by Dr. Kenji Arakawa in the 1970s. He was the first to discover that internal organ systems ..</p>
  </div>
  <div class="abs card" style="left:683px">
    <div class="card-head">ACUPUNCTURE</div>
    <div class="card-img" role="img" aria-label="Photo of a woman lying on a treatment table with a practitioner" style="background:linear-gradient(90deg,#ecebe8,#e2bfa2 45%,#f1ddcc)"></div>
    <p>While pursuing a degree in premedicine &amp; behavior science at the State U, Morgan learned the benefits of Chinese medicine</p>
  </div>

  <h3 class="abs products-title" style="font-weight:400">Our Products</h3>
  <div class="abs product" style="left:118px">
    <div class="product-img" role="img" aria-label="Photo of candles and rolled towels" style="background:linear-gradient(135deg,#dfe9c8,#f4f4ea 50%,#b9cf6a)"></div>
    <div class="product-name">Lorem ipsum dolor sit ame</div><div class="product-sub">Consectetuer elit....</div>
    <div class="product-row"><span class="price">$30.99</span><span class="cart">Add to cart</span></div>
  </div>
  <div class="abs product" style="left:329px">
    <div class="product-img" role="img" aria-label="Photo of lavender, lemon slices and an oil bottle" style="background:linear-gradient(135deg,#f3e7c9,#c9a878 50%,#8f86b8)"></div>
    <div class="product-name">Lorem ipsum dolor sit ame</div><div class="product-sub">Consectetuer elit....</div>
    <div class="product-row"><span class="price">$25.99</span><span class="cart">Add to cart</span></div>
  </div>
  <div class="abs product" style="left:537px">
    <div class="product-img" role="img" aria-label="Photo of spa towels and lit candles" style="background:linear-gradient(135deg,#5a3a2a,#e9e0d2 45%,#c84a22)"></div>
    <div class="product-name">Lorem ipsum dolor sit ame</div><div class="product-sub">Consectetuer elit....</div>
    <div class="product-row"><span class="price">$35.99</span><span class="cart">Add to cart</span></div>
  </div>
  <div class="abs product" style="left:743px">
    <div class="product-img" role="img" aria-label="Photo of a white flower with a wooden bowl and leaves" style="background:linear-gradient(135deg,#f7f4dc,#7fa53a 50%,#a86a3a)"></div>
    <div class="product-name">Lorem ipsum dolor sit ame</div><div class="product-sub">Consectetuer elit....</div>
    <div class="product-row"><span class="price">$50.99</span><span class="cart">Add to cart</span></div>
  </div>

  <div class="abs footer"></div>
  <div class="abs foot-nav">So Tai Ho &nbsp;| &nbsp;Seitai Shinpo &nbsp;| &nbsp;Acupuncture &nbsp;| &nbsp;Biography &nbsp;| &nbsp;Nutrition &nbsp;| &nbsp;My Journey &nbsp;| &nbsp;Contact Us</div>
  <div class="abs copy">Copyright 2012 © Lotus Ridge Acupuncture — All Rights Reserved</div>
</div>
</body>
</html>
```